Beautiful, sharp, website design for family-run property development company.

We are property developers in Kent (south east of London) who want to see the local town change. We are the only local property developer that is a family run business, focussing primarily on converting old, dilapidated Victorian buildings into beautiful residential spaces. Unlike other national developers, we work to regenerate buildings to create new employment opportunities, housing, and revive the town Centre .

Target Market(s)

1. Investors and Joint Venture partners - people with money to invest in property
2. Buyers of property - 25 to 40 year old, young professionals.
3. Commercial funders (people lending money to our projects
4. Professional team: Architects, builders, Estate agent who want to work with us

Industry/Entity Type

Real Estate Development

Coding

Number of Pages Required

Font styles to use
• Please follow the brief of stylish, elegant, modern

Colors

Designer to choose colors to be used in the design.

Requirements
Must have
• Please use these websites as a reference of what we are looking to achieve.
• http://brekmorestudio.com/#page5
• https://palvendro.co.uk/
• http://tamberfold.co.uk/
• http://www.thequarvishgroup.co.uk/about-quarvish
• Clean, simple, elegant, minimal design.
• Images of interiors of houses that have been converted from old buildings
• Images of farm buildings e.g. barns that have been converted to new homes or offices. Images of properties that may have been an old factory or old commercial property that is now a trendy apartment.
• Please use images of properties and interiors that are from the South East of England (including Kent, Surrey, Sussex, Hampshire, Dorset). There is a distinct style of housing in this part of England.
Nice to have
• Colours consistent with our brand colour palette (attached)

```html
<!DOCTYPE html>
<html lang="en">
<head>
<meta charset="utf-8">
<title>Garnet Elm Property</title>
<link rel="stylesheet" href="https://fonts.googleapis.com/css2?family=Montserrat:wght@400;500;600;700;800&display=swap">
<style>
:root{
  --header-bg:#f2f2f2;
  --ink:#1f1f1f;
  --sage:#8aa39b;
  --slate:#5f716c;
  --slate-dark:#26302d;
  --mint:#f1f5ec;
  --stone:#8e9b98;
  --footer:#231f20;
  --footer-text:#f2f2f2;
  --logo:#6f8a83;
  --dot:#c9cfcd;
  --white:#ffffff;
}
*{margin:0;padding:0;box-sizing:border-box}
html,body{width:1200px;height:2748px;overflow:hidden}
body{position:relative;background:var(--white);font-family:'Montserrat',sans-serif;color:var(--ink)}
.abs{position:absolute}
.dotted{background-color:var(--white);background-image:radial-gradient(circle,var(--dot) 1.2px,transparent 1.6px);background-size:34px 34px}
.photo{position:absolute}

/* header */
.site-header{left:0;top:0;width:1200px;height:137px;background:var(--header-bg)}
.brand{left:47px;top:78px;font-size:24px;font-weight:600;letter-spacing:1px;color:var(--logo);display:flex;align-items:center;gap:10px}
.brand .mark{width:14px;height:14px;border-radius:50%;background:var(--logo)}
.nav{top:60px;font-size:20px;font-weight:500;letter-spacing:1.2px;color:var(--ink)}

/* hero */
.hero-title{left:47px;top:272px;font-size:37px;font-weight:700;letter-spacing:2px;line-height:46px}
.hero-title .accent{color:var(--sage);display:block}
.hero-copy{left:43px;top:373px;width:420px;font-size:14px;font-weight:500;line-height:17px;letter-spacing:.5px}
.hero-bar{left:582px;width:4px;background:var(--ink)}
.hero-photo{left:600px;top:137px;width:600px;height:443px;background:linear-gradient(160deg,#e6e8e6 0%,#c9cbc6 45%,#a48f78 80%,#6a4f3a 100%)}

/* developers */
.dev-dots{left:0;top:580px;width:576px;height:448px}
.frame{position:absolute;border:4px solid var(--ink)}
.dev-photo{left:162px;top:652px;width:234px;height:317px;background:linear-gradient(170deg,#b79a7a 0%,#2f4a3c 40%,#5b6b4f 65%,#e4e2dd 100%)}
.dev-panel{left:576px;top:580px;width:624px;height:448px;background:var(--slate)}
.dev-title{left:630px;top:668px;font-size:25px;font-weight:800;letter-spacing:2.4px;line-height:34px;color:var(--slate-dark)}
.dev-title .light{color:var(--white)}
.dev-copy{left:627px;top:767px;width:510px;font-size:14.5px;line-height:18.4px;letter-spacing:.5px;color:var(--white)}

/* connect */
.connect-panel{left:0;top:1028px;width:581px;height:450px;background:var(--mint)}
.connect-title{left:37px;top:1163px;font-size:30px;font-weight:700;letter-spacing:3px;line-height:37px}
.connect-title .accent{color:var(--sage);display:block}
.connect-copy{left:38px;top:1247px;width:520px;font-size:17.5px;line-height:21px;letter-spacing:.6px}
.connect-dots{left:581px;top:1028px;width:619px;height:450px}
.connect-photo{left:675px;top:1117px;width:409px;height:273px;background:linear-gradient(180deg,#eeeeec 0%,#d9d6cf 50%,#b98a4e 78%,#a87740 100%)}

/* gallery */
.g1{left:16px;top:1527px;width:365px;height:244px;background:linear-gradient(180deg,#c7d3df 0%,#9a4a34 45%,#7d6150 75%,#9a9a98 100%)}
.g2{left:386px;top:1527px;width:365px;height:244px;background:linear-gradient(170deg,#6e4a30 0%,#e9e7e4 45%,#f3f3f3 65%,#1e1e22 100%)}
.g3{left:16px;top:1777px;width:365px;height:242px;background:linear-gradient(160deg,#7a4a2a 0%,#f1efec 45%,#f6f6f6 70%,#a8714a 100%)}
.g4{left:386px;top:1777px;width:365px;height:242px;background:linear-gradient(180deg,#6e4a30 0%,#ece9e5 40%,#f4f3f1 70%,#d8d2c9 100%)}

/* regions */
.regions-back{left:924px;top:1616px;width:231px;height:379px;background:var(--stone)}
.regions-box{left:831px;top:1554px;width:255px;height:411px;border:7px solid var(--ink);background-color:var(--white);background-image:radial-gradient(circle,var(--dot) 1.2px,transparent 1.6px);background-size:24px 24px}
.regions-dot{left:793px;top:1507px;width:90px;height:90px;border-radius:50%;background:var(--footer)}
.regions-list{left:868px;top:1632px;list-style:none;font-size:30px;letter-spacing:1.5px;line-height:44px}
.regions-list li::before{content:"";display:inline-block;width:11px;height:11px;border-radius:50%;background:var(--ink);margin-right:12px;vertical-align:middle;position:relative;top:-5px}

/* quote */
.quote-band{left:0;top:2069px;width:1200px;height:330px;background-color:var(--slate);background-image:radial-gradient(circle,#75857f 1.2px,transparent 1.6px);background-size:30px 30px}
.quote{left:40px;top:2170px;width:1120px;text-align:center;font-size:29px;font-weight:700;letter-spacing:1.2px;line-height:35px;color:var(--slate-dark)}

/* footer */
.site-footer{left:0;top:2459px;width:1200px;height:289px;background:var(--footer)}
.footer-brand{left:30px;top:2610px;font-size:30px;font-weight:600;letter-spacing:1px;color:var(--logo);display:flex;align-items:center;gap:12px}
.footer-brand .mark{width:16px;height:16px;border-radius:50%;background:var(--logo)}
.about-title{left:375px;top:2524px;font-size:28px;font-weight:600;letter-spacing:2.5px;color:var(--footer-text)}
.about-copy{left:369px;top:2599px;width:340px;font-size:16px;font-weight:600;line-height:21px;letter-spacing:.6px;color:var(--footer-text)}
.contact-item{left:793px;display:flex;align-items:center;gap:18px;font-size:20px;letter-spacing:1.2px;color:var(--footer-text)}
.contact-item svg{width:36px;height:36px;flex:none}
</style>
</head>
<body>

<header class="abs site-header">
  <div class="abs brand"><span class="mark"></span>GARNET ELM</div>
  <nav>
    <span class="abs nav" style="left:703px">HOME</span>
    <span class="abs nav" style="left:797px">PROJECTS</span>
    <span class="abs nav" style="left:941px">ABOUT</span>
    <span class="abs nav" style="left:1053px">CONTACT</span>
  </nav>
</header>

<section class="hero">
  <h1 class="abs hero-title">Redesign your<span class="accent">PROPERTY</span></h1>
  <p class="abs hero-copy">At Garnet Elm we develop beautiful and unique properties in and around South London. We strive for perfection and never stop challenging ourselves.</p>
  <div class="abs hero-bar" style="top:137px;height:93px"></div>
  <div class="abs hero-bar" style="top:528px;height:52px"></div>
  <div class="photo hero-photo" role="img" aria-label="Bright modern open-plan living room with sofa, coffee table and kitchen"></div>
</section>

<section class="developers">
  <div class="abs dev-dots dotted"></div>
  <div class="frame" style="left:193px;top:638px;width:219px;height:343px"></div>
  <div class="photo dev-photo" role="img" aria-label="Cosy café-style interior with dark green wall, plants and wooden seating"></div>
  <div class="abs dev-panel"></div>
  <h2 class="abs dev-title">PROPERTY DEVELOPERS IN<br><span class="light">SOUTH (East of London)</span></h2>
  <p class="abs dev-copy">We’ve been developing properties in and around South London for the last 4 years. We are a small team of dedicated professionals and we ensure that our exacting standards are met throughout the whol design and build process. The end results are properties that challenge conventions and redefine the norm. If you would like to know more about any of our developments then please get in touch</p>
</section>

<section class="connect">
  <div class="abs connect-panel"></div>
  <h2 class="abs connect-title">CONNECT WITH<span class="accent">GARNET ELM</span></h2>
  <p class="abs connect-copy">We’ve been developing properties in and around South London for the last 4 years. We are a small team of dedicated professionals</p>
  <div class="abs connect-dots dotted"></div>
  <div class="frame" style="left:746px;top:1101px;width:356px;height:307px"></div>
  <div class="photo connect-photo" role="img" aria-label="Light apartment with white kitchen, dining table, sofa and wooden floor"></div>
</section>

<section class="gallery">
  <div class="photo g1" role="img" aria-label="Red-brick Victorian building on a street corner"></div>
  <div class="photo g2" role="img" aria-label="Converted Victorian hall with timber roof beams and open living space"></div>
  <div class="photo g3" role="img" aria-label="Bedroom under exposed wooden roof trusses"></div>
  <div class="photo g4" role="img" aria-label="Bathroom with freestanding tub beneath timber beams"></div>
</section>

<section class="regions">
  <div class="abs regions-back"></div>
  <div class="abs regions-box"></div>
  <div class="abs regions-dot"></div>
  <ul class="abs regions-list">
    <li>Kent</li>
    <li>Surrey</li>
    <li>Sussex</li>
    <li>Dorset</li>
    <li>Hampshire</li>
  </ul>
</section>

<section class="abs quote-band"></section>
<blockquote class="abs quote">“We are the only local property developer that is a family run business, focussing primarily on converting old, dilapidated Victorian buildings into beautiful residential spaces”</blockquote>

<footer class="abs site-footer"></footer>
<div class="abs footer-brand"><span class="mark"></span>GARNET ELM</div>
<h3 class="abs about-title">ABOUT US</h3>
<p class="abs about-copy">We are property developers in Kent (south east of London) who want to see the local town change.</p>

<div class="abs contact-item" style="left:793px;top:2520px">
  <svg viewBox="0 0 36 36" style="margin-left:-2px"><rect x="2" y="7" width="32" height="22" fill="#7f8a88"/><path d="M2 7 L18 20 L34 7 M2 29 L14 17 M34 29 L22 17" stroke="#231f20" stroke-width="2" fill="none"/></svg>
  <span>garnetelm@postmail.com</span>
</div>
<div class="abs contact-item" style="left:793px;top:2573px">
  <svg viewBox="0 0 36 36"><path d="M18 2 C10 2 5 8 5 15 C5 24 18 35 18 35 C18 35 31 24 31 15 C31 8 26 2 18 2 Z" fill="#7f8a88"/><circle cx="18" cy="15" r="5" fill="#231f20"/></svg>
  <span>R 12 Street, Fen Road</span>
</div>
<div class="abs contact-item" style="left:793px;top:2639px">
  <svg viewBox="0 0 36 36"><path d="M8 3 L14 3 L16 11 L12 14 C14 19 17 22 22 24 L25 20 L33 22 L33 28 C33 31 30 33 27 33 C14 31 5 22 3 9 C3 6 5 3 8 3 Z" fill="#7f8a88"/></svg>
  <span>70001234567</span>
</div>

</body>
</html>
```